Postcard for Antique Furniture Restorer

My business is to restore antique furniture. I am based in Sydney, Australia.

I will be using this postcard to promote my business.
I will give it to customers like a With Compliments card.

Sometimes I will be writing information on the back of the card.

Design for Postcard Size eg 148 X 105mm

Front of card:

Attached are images of Antique furniture - please use ONLY 1 of the 3 images.
Deep etch the image on a white or cream background.

On front of card add these words:
Timber Reborn
antique furniture restoration

Antiques travel through time, seeing generations of families
Through time they remain - they tell a continuing story
Be part of the journey

Back of postcard:
(leave space for notes to be handwritten)

Add these words:

Timber Reborn
Corin Maddox
mobile 0437 552 618
www.oakandvarnishcraft.com.au

Industry/Entity Type

Business

Font styles to use
Serif
Sans Serif

Colors
fefdec
ffffff

Requirements
Must have
• Use only 1 image. Image must be deep etched.

```html
<!DOCTYPE html>
<html lang="en">
<head>
<meta charset="utf-8">
<title>Timber Reborn – Postcard</title>
<link rel="stylesheet" href="https://fonts.googleapis.com/css2?family=Gelasio:wght@400;500&display=swap">
<style>
  :root {
    --page-bg: #e9e6e1;
    --card-white: #ffffff;
    --parchment-light: #f1e2c2;
    --parchment-mid: #e2c99c;
    --parchment-deep: #c9a877;
    --ink-soft: #7a4a33;
    --ink-deep: #4a1e10;
    --rule-brown: #7a3a22;
    --wood-dark: #5e2414;
    --wood-mid: #8a3c22;
  }
  * { margin: 0; padding: 0; box-sizing: border-box; }
  html, body {
    width: 1200px; height: 1000px; overflow: hidden;
    background: var(--page-bg);
    font-family: "Gelasio", Georgia, serif;
  }
  .canvas { position: relative; width: 1200px; height: 1000px; }

  /* Back of card */
  .card-back {
    position: absolute; left: 465px; top: 492px;
    width: 700px; height: 496px;
    background: var(--card-white);
  }
  .card-back__divider {
    position: absolute; left: 406px; top: 0;
    width: 2px; height: 100%; background: var(--rule-brown);
  }
  .card-back__stamp {
    position: absolute; left: 572px; top: 32px;
    width: 95px; height: 98px;
    border: 1.5px solid var(--rule-brown);
  }
  .card-back__address-line {
    position: absolute; left: 431px; width: 247px;
    height: 2px; background: var(--rule-brown);
  }
  .card-back__contact {
    position: absolute; left: 32px; top: 334px;
    color: var(--ink-deep); font-size: 19px; line-height: 24.5px;
  }
  .card-back__name { font-size: 25px; line-height: 30px; }

  /* Front of card */
  .card-front {
    position: absolute; left: 52px; top: 12px;
    width: 708px; height: 501px;
    background: var(--card-white);
    padding: 14px 14px 15px 14px;
  }
  .card-front__artwork {
    position: relative; width: 680px; height: 472px; overflow: hidden;
  }
  .card-front__pattern {
    position: absolute; inset: 0;
    background: radial-gradient(ellipse at 50% 55%, var(--parchment-light) 0%, var(--parchment-mid) 60%, var(--parchment-deep) 100%);
  }
  .card-front__tagline {
    position: absolute; left: 0; width: 100%; top: 40px;
    text-align: center; color: var(--ink-soft);
    font-size: 19px; line-height: 23px;
  }
  .card-front__invite {
    position: absolute; left: 0; width: 100%; top: 96px;
    text-align: center; color: var(--ink-soft); font-size: 24px;
  }
  .card-front__furniture {
    position: absolute; left: 148px; top: 152px;
    width: 390px; height: 222px;
    background: linear-gradient(135deg, var(--wood-mid), var(--wood-dark));
    border-radius: 3px;
  }
  .card-front__brand {
    position: absolute; left: 0; width: 100%; top: 380px;
    text-align: center; color: var(--ink-deep);
    font-size: 40px; line-height: 48px;
  }
  .card-front__service {
    position: absolute; left: 0; width: 100%; top: 427px;
    text-align: center; color: var(--ink-deep);
    font-size: 21px; line-height: 26px;
  }
</style>
</head>
<body>
<div class="canvas">

  <section class="card-back" aria-label="Postcard back">
    <div class="card-back__divider"></div>
    <div class="card-back__stamp"></div>
    <div class="card-back__address-line" style="top:196px"></div>
    <div class="card-back__address-line" style="top:248px"></div>
    <div class="card-back__address-line" style="top:304px"></div>
    <div class="card-back__address-line" style="top:365px"></div>
    <div class="card-back__contact">
      <div class="card-back__name">Timber Reborn</div>
      <div>antique furniture restoration</div>
      <div>Corin Maddox</div>
      <div>mobile 0437 552 618</div>
      <div>www.oakandvarnishcraft.com.au</div>
    </div>
  </section>

  <section class="card-front" aria-label="Postcard front">
    <div class="card-front__artwork">
      <div class="card-front__pattern" role="img" aria-label="Aged parchment damask wallpaper pattern"></div>
      <p class="card-front__tagline">Antiques travel through time, seeing generations of families<br>Through time they remain , they tell a continuing story...</p>
      <p class="card-front__invite">Be part of the journey</p>
      <div class="card-front__furniture" role="img" aria-label="Two restored mahogany chests of drawers with inlaid drawer fronts and brass handles"></div>
      <h1 class="card-front__brand" style="font-weight:400">Timber Reborn</h1>
      <p class="card-front__service">antique furniture restoration</p>
    </div>
  </section>

</div>
</body>
</html>
```